Supplement Treats for Dogs and Cats Needs a Label Design

Hello everyone,We are looking for a label design for our new product. We have the container already.Attached you'll find a rough draft of the label we want, along with our logo, and the the animals we would like featured on the label. We will send along the texts, the supplement facts, QRB statement, address, and barcode once as soon as they're ready. For now, we'd like to see a more polished design.Label Measurement: 28cm x 7 cmWe might have some stock photos we want to use, I will attach it later when I have bought them. Please wait before submitting.
MIDDLE AGE

```html
<!DOCTYPE html>
<html lang="en">
<head>
<meta charset="utf-8">
<title>Tailwise Calming Chews – Label</title>
<link rel="stylesheet" href="https://fonts.googleapis.com/css2?family=Anton&family=Lato:ital,wght@0,400;0,700;0,900;1,700;1,900&family=Open+Sans:ital,wght@0,400;0,600;1,400;1,600&display=swap">
<style>
:root{
  --brown:#5b2a23;
  --brown-dark:#4a211b;
  --orange:#f2692f;
  --orange-soft:#f6b35a;
  --grey-light:#eef0f2;
  --grey-mid:#c9ced3;
  --ink:#2b2b2b;
  --white:#ffffff;
  --gold:#e2b233;
  --stage:#3a3a3a;
}
*{box-sizing:border-box;margin:0;padding:0}
html,body{width:1200px;height:1006px;overflow:hidden;background:var(--stage)}
.label{
  position:absolute;left:20px;top:357px;
  width:1375px;height:345px;
  transform:scale(0.8436);transform-origin:0 0;
  background:linear-gradient(90deg,var(--grey-light) 0%,#dfe2e5 40%,var(--grey-mid) 62%,#e9ebed 72%,var(--white) 74%);
  overflow:hidden;font-family:"Open Sans",sans-serif;color:var(--ink);
}
.label-shapes{position:absolute;inset:0}
.abs{position:absolute}
.tagline{left:30px;top:24px;font:italic 900 19px "Lato",sans-serif;color:var(--brown)}
.intro{left:30px;top:50px;font-size:10px;line-height:12.5px;white-space:nowrap}
.why{left:30px;top:91px;font:italic 900 15px "Lato",sans-serif;color:var(--brown)}
.feeding{left:30px;top:114px;font-size:10px;line-height:12.5px;white-space:nowrap}
.feeding em{font-style:italic;font-weight:600}
.warning{left:28px;top:172px;width:380px;height:51px;border:2px solid var(--brown);border-radius:0 12px 12px 0;padding:5px 10px;font:italic 600 10px/13.5px "Open Sans",sans-serif;white-space:nowrap;background:var(--white)}
.distributor{left:30px;top:258px;font:italic 900 16px "Lato",sans-serif;color:var(--white)}
.lorem{left:30px;top:282px;width:300px;font-size:13px;line-height:17px;color:var(--white)}
.brand{left:560px;top:44px;display:flex;align-items:center;gap:10px;font:400 40px "Anton",sans-serif;color:var(--brown);letter-spacing:2px}
.brand-dot{width:34px;height:34px;border-radius:50%;background:var(--brown)}
.product{left:492px;top:112px;font:400 84px/92px "Anton",sans-serif;color:var(--brown);letter-spacing:1px}
.audience{left:493px;top:204px;width:255px;height:36px;background:var(--orange);color:var(--white);font:700 22px/36px "Lato",sans-serif;padding-left:22px}
.count{left:494px;top:266px;font:900 24px/26px "Lato",sans-serif;color:var(--brown)}
.count span{background:var(--orange);color:var(--white);padding:0 3px;border-radius:4px}
.chewable{left:494px;top:294px;font:italic 900 11px "Lato",sans-serif;color:var(--brown)}
.weight{left:494px;top:310px;font:700 15px "Lato",sans-serif;color:var(--ink)}
.facts{left:1036px;top:25px;width:244px;height:200px;border:2px solid var(--brown);padding:3px;background:var(--white)}
.facts-inner{border:1px solid var(--brown);height:100%;padding:6px 6px}
.facts-title{font:400 21px "Anton",sans-serif;color:var(--brown);border-bottom:4px solid var(--brown);padding-bottom:2px}
.facts-head{font:600 10px "Open Sans",sans-serif;padding:8px 0 2px;border-bottom:2px solid var(--brown)}
.facts-row{display:flex;justify-content:space-between;font-size:10px;line-height:15px;border-bottom:1px solid var(--brown)}
.others{left:1023px;top:247px;width:337px;height:73px;border:2px solid var(--brown);padding:5px 8px;font-size:9.6px;line-height:12.5px;background:var(--white)}
.others b{font-weight:600}
</style>
</head>
<body>
<div class="label">
  <svg class="label-shapes" viewBox="0 0 1375 345" width="1375" height="345">
    <polygon points="960,0 1005,0 860,345 815,345" fill="var(--orange-soft)"/>
    <polygon points="1005,0 1040,0 895,345 860,345" fill="var(--orange)"/>
    <polygon points="1040,0 1110,0 1040,70 1000,70" fill="var(--brown)"/>
    <polygon points="0,233 493,233 433,345 0,345" fill="var(--brown)"/>
    <circle cx="386" cy="283" r="42" fill="#d6d9dc" stroke="var(--white)" stroke-width="4"/>
    <circle cx="920" cy="112" r="52" fill="var(--gold)"/>
    <rect x="604" y="252" width="72" height="48" rx="18" fill="#c59a62" role="img" aria-label="Bone-shaped soft chew treats"/>
    <rect x="700" y="165" width="290" height="180" fill="url(#photo)" role="img" aria-label="Golden retriever and grey cat cuddling beside a white bowl"/>
    <defs>
      <radialGradient id="photo" cx="50%" cy="60%" r="60%">
        <stop offset="0%" stop-color="#b46a2e"/>
        <stop offset="60%" stop-color="#8c8c92"/>
        <stop offset="100%" stop-color="#dcdfe2" stop-opacity="0"/>
      </radialGradient>
    </defs>
  </svg>

  <div class="abs tagline">MADE WITH THAT TASTE PETS LOVE</div>
  <p class="abs intro">Our calming formula is specially formulated to help dogs and cats relax under times<br>of increased stress. It's comprised of all natural ingredients, to create delicious<br>chewable treat.</p>
  <div class="abs why">WHY IT WORK:</div>
  <p class="abs feeding"><em>Feeding directions:</em> Cats and dogs up to 25 lbs, 1 chew daily. For medium and large dogs<br>26-50 lbs, 2 chews daily. For 51-100 lbs, 3 chews daily. For over 100 lbs, 4 chews daily.<br>No artificial colors or preservatives.<br>Store in a cool, dry place.</p>
  <div class="abs warning">For animal use only, keep out of the reach of children.<br>In case of accidental overdose contact a health professional immediately<br>This product is intended for supplemental use.</div>
  <div class="abs distributor">Distributed by NORVANE LLC.</div>
  <p class="abs lorem">Lorem ipsum dolor sit amet, consectetuer adipiscing elit, sed diam nonummy nibh euismod</p>

  <div class="abs brand"><span class="brand-dot"></span>TAILWISE</div>
  <div class="abs product">CALMING</div>
  <div class="abs audience">FOR DOGS AND CATS</div>
  <div class="abs count"><span>60</span> SOFT</div>
  <div class="abs chewable">CHEWABLE TREATS</div>
  <div class="abs weight">Net Weight. 8 oz. (226.8 g.)</div>

  <div class="abs facts"><div class="facts-inner">
    <div class="facts-title">SUPPLEMENT FACTS</div>
    <div class="facts-head">Active Ingredients</div>
    <div class="facts-row"><span>Thiamine</span><span>25mg</span></div>
    <div class="facts-row"><span>Chamomile</span><span>50mg</span></div>
    <div class="facts-row"><span>L-Theanine</span><span>25mg</span></div>
    <div class="facts-row"><span>Ginger Root</span><span>25mg</span></div>
    <div class="facts-row"><span>ValerianRoot</span><span>10mg</span></div>
    <div class="facts-row"><span>PassionFlower</span><span>10mg</span></div>
    <div class="facts-row"><span>L-Tryptophan</span><span>10mg</span></div>
  </div></div>
  <p class="abs others"><b>Other Ingredients:</b> Brewer'sYeast,ChickpeaFlour, Glycerin, Tapioca Starch, PurifiedWater, SunflowerLecithin, ChickenPowder, Fish Oil, ChamomilePowder, ThiamineMononitrate, SafflowerOil, L-Theanine, GingerRoot, L-Tryptophan, ValerianRoot, PassionFlower, SorbicAcid, MixedTocopherols, AscorbicAcid.</p>
</div>
</body>
</html>
```